Production Co Needs Movie Poster for Supernatural Thriller

Hi, we need a poster designed for a film we're going to be pitching and raising finance for. The film is a supernatural thriller called "Where the Lanterns Sleep", a story told from the perspective of the ghosts - a father and his 8 year old son. References include 'Beneath the Quiet Orchard' (reference poster attached) and 'The Hollow Lighthouse' - not blood and gore but creepy and atmospheric. We're looking for a design that will capture the imagination and make people want to know more and see the movie!

Synopsis:
When the sudden deaths of young Tobias and his father render them as ghosts, they’re thrust into a dangerous new reality of amateur clairvoyants, determined ghost hunters, and lost souls; a plane of existence where they must survive both the living and the dead.

Industry/Entity Type

Finance

Requirements
Nice to have
• It would be nice to include the father/son imagery perhaps in silhouette. Open to ideas. The film is a psychological thriller as much as a ghost story so it would be good to include that element rather than a 'traditional horror' style poster.
• Alternatively a simple, striking image with the title would also be great - see Kestrel poster attached as a reference,
• ALSO - the entire film takes place inside the house.
Should not have
• No screaming faces please.

```html
<!DOCTYPE html>
<html lang="en">
<head>
<meta charset="UTF-8">
<title>Where the Lanterns Sleep — Poster</title>
<link rel="stylesheet" href="https://fonts.googleapis.com/css2?family=Nanum+Brush+Script&family=Roboto:wght@300&display=swap">
<style>
  :root {
    --paper-base: #c6c5c3;
    --paper-stain: rgba(90, 90, 88, 0.35);
    --paper-light: rgba(235, 235, 232, 0.6);
    --night: #040404;
    --wall-light: rgba(190, 176, 158, 0.6);
    --wall-mid: rgba(150, 138, 124, 0.3);
    --figure-warm: rgba(150, 96, 76, 0.42);
    --crease: rgba(0, 0, 0, 0.35);
    --title-ink: #d2cec9;
    --tagline-red: #6a2820;
  }
  * { margin: 0; padding: 0; box-sizing: border-box; }
  html, body {
    width: 900px;
    height: 1200px;
    overflow: hidden;
    background: var(--paper-base);
  }
  .poster {
    position: relative;
    width: 900px;
    height: 1200px;
    background:
      radial-gradient(circle at 12% 4%, var(--paper-stain), transparent 9%),
      radial-gradient(circle at 88% 2%, var(--paper-stain), transparent 7%),
      radial-gradient(circle at 98% 45%, var(--paper-stain), transparent 6%),
      radial-gradient(circle at 1% 62%, var(--paper-stain), transparent 7%),
      radial-gradient(circle at 60% 99%, var(--paper-stain), transparent 8%),
      radial-gradient(circle at 20% 98%, var(--paper-light), transparent 8%),
      radial-gradient(circle at 97% 80%, var(--paper-light), transparent 6%),
      radial-gradient(circle at 40% 1%, var(--paper-light), transparent 7%),
      repeating-linear-gradient(37deg, rgba(0,0,0,0.04) 0 2px, transparent 2px 7px),
      repeating-linear-gradient(-61deg, rgba(255,255,255,0.05) 0 1px, transparent 1px 5px),
      var(--paper-base);
  }
  .poster__field {
    position: absolute;
    left: 28px;
    top: 28px;
    right: 28px;
    bottom: 28px;
    background: var(--night);
    overflow: hidden;
  }
  .poster__photo {
    position: absolute;
    inset: 0;
    background:
      radial-gradient(farthest-side at 50% 50%, var(--figure-warm), transparent) 330px 300px / 260px 560px no-repeat,
      radial-gradient(farthest-side at 50% 50%, rgba(140, 86, 68, 0.32), transparent) 560px 420px / 160px 420px no-repeat,
      linear-gradient(200deg, transparent 30%, var(--night) 72%),
      linear-gradient(114deg, transparent 36%, var(--wall-mid) 46%, var(--wall-light) 58%, var(--wall-mid) 68%, transparent 78%);
  }
  .poster__crease {
    position: absolute;
    background: var(--crease);
  }
  .poster__crease--vertical { left: 420px; top: 140px; width: 1px; height: 480px; }
  .poster__crease--horizontal { left: 300px; top: 600px; width: 340px; height: 1px; }
  .poster__title {
    position: absolute;
    left: 0;
    right: 0;
    top: 790px;
    padding-left: 40px;
    text-align: center;
    font-weight: normal;
  }
  .title__line {
    display: block;
    font-family: "Nanum Brush Script", cursive;
    color: var(--title-ink);
    text-transform: uppercase;
    line-height: 0.95;
  }
  .title__line--small { font-size: 62px; letter-spacing: 1px; }
  .title__line--large { font-size: 84px; letter-spacing: 2px; }
  .title__tag {
    display: block;
    margin-top: 12px;
    font-family: "Roboto", Arial, sans-serif;
    font-weight: 300;
    font-size: 30px;
    color: var(--tagline-red);
  }
</style>
</head>
<body>
  <main class="poster">
    <div class="poster__field">
      <div class="poster__photo" role="img" aria-label="Photograph of a father and son seen as faint shadowy silhouettes in a shaft of light across a cracked wall"></div>
      <div class="poster__crease poster__crease--vertical"></div>
      <div class="poster__crease poster__crease--horizontal"></div>
      <h1 class="poster__title">
        <span class="title__line title__line--small">Where the</span>
        <span class="title__line title__line--large">Lanterns</span>
        <span class="title__tag">sleep</span>
      </h1>
    </div>
  </main>
</body>
</html>
```